11 x 11 Flyer Design for Social Media - Reverse Mortgages

62 or older?

A Reverse Mortgage
could be
Your Road to Financial Freedom

* No Monthly Payments
* No Income Requirements
* No Credit Score Requirements
* No Loss of Ownership

Receive cash by lump sum, monthly installments or a line of credit!!

Call us today for a Free Consultation!!
(800) 471-2965

Bluegate Financial Services, Inc.
NMLS #318760
www.bluegatehome.com

```html
<!DOCTYPE html>
<html lang="en">
<head>
<meta charset="utf-8">
<title>Reverse Mortgage Flyer – Bluegate Financial Services</title>
<link rel="stylesheet" href="https://fonts.googleapis.com/css2?family=Arimo:wght@700&family=Roboto+Condensed:wght@700&display=swap">
<style>
  :root {
    --stage: #1c1c1c;
    --paper: #ffffff;
    --brand-blue: #1f5fae;
    --brand-red: #e21f26;
    --ink: #111111;
    --skin-warm: #8a5a3c;
    --skin-deep: #5b3a26;
    --sky: #a9cfe0;
    --shirt-light: #e8e6e1;
  }
  * { box-sizing: border-box; margin: 0; padding: 0; }
  html, body {
    width: 1200px; height: 870px; overflow: hidden;
    background: var(--stage);
  }
  .canvas {
    position: relative; width: 1200px; height: 870px;
    display: flex; align-items: center; justify-content: center;
  }
  .flyer {
    position: relative; width: 625px; height: 625px;
    background: var(--paper);
    transform: scale(1.32);
    overflow: hidden;
    font-family: "Arimo", Arial, sans-serif;
    color: var(--ink);
  }
  .headline {
    position: absolute; left: 33px; top: 22px;
    font-family: "Roboto Condensed", "Arial Narrow", sans-serif;
    font-weight: 700; font-size: 29px; line-height: 36px;
    color: var(--brand-red); letter-spacing: 0.1px;
  }
  .age-arrow { position: absolute; left: 414px; top: 0; width: 180px; height: 202px; }
  .age-text {
    position: absolute; left: 442px; top: 14px; width: 150px;
    text-align: center; color: var(--paper); font-weight: 700;
  }
  .age-text .age-number { display: block; font-size: 56px; line-height: 54px; }
  .age-text .age-or { display: block; font-size: 25px; line-height: 24px; }
  .age-text .age-older { display: block; font-size: 25px; line-height: 28px; }
  .benefits {
    position: absolute; left: 47px; top: 104px; list-style: none;
    font-size: 18px; line-height: 25.6px;
  }
  .benefits li::before {
    content: ""; display: inline-block; width: 7px; height: 7px;
    background: var(--brand-blue); transform: rotate(45deg);
    margin: 0 4px 3px 1px;
  }
  .payout {
    position: absolute; left: 33px; top: 219px;
    font-size: 17.5px; line-height: 25px;
  }
  .company {
    position: absolute; left: 330px; top: 236px; width: 270px; text-align: center;
    font-family: "Roboto Condensed", "Arial Narrow", sans-serif; font-weight: 700;
  }
  .company-name { font-size: 18px; line-height: 22px; color: var(--ink); }
  .company-license { font-size: 17px; line-height: 24px; color: var(--brand-red); }
  .contact { position: absolute; left: 30px; top: 313px; }
  .contact-cta {
    font-family: "Roboto Condensed", "Arial Narrow", sans-serif; font-weight: 700;
    font-size: 13.5px; color: var(--brand-blue); padding-left: 1px;
  }
  .contact-phone { font-size: 30px; line-height: 36px; color: var(--brand-red); font-weight: 700; }
  .collage { position: absolute; left: 0; top: 0; width: 625px; height: 625px; pointer-events: none; }
  .collage .photo { pointer-events: auto; }
  .web-band {
    position: absolute; left: 0; bottom: 0; width: 625px; height: 48px;
    background: var(--brand-blue); color: var(--paper);
    font-size: 30px; line-height: 48px; text-align: center; letter-spacing: 2.6px;
  }
</style>
</head>
<body>
<main class="canvas">
  <article class="flyer">
    <h1 class="headline">A Reverse Mortgage could be<br>Your Road to Financial Freedom</h1>

    <svg class="age-arrow" viewBox="0 0 180 202" aria-hidden="true">
      <polygon points="28,0 178,0 178,102 180,102 106,202 0,102 28,102" fill="var(--brand-blue)"/>
    </svg>
    <p class="age-text">
      <span class="age-number">62</span>
      <span class="age-or">or</span>
      <span class="age-older">OLDER?</span>
    </p>

    <ul class="benefits">
      <li>No Monthly Payments</li>
      <li>No Income Requirements</li>
      <li>No Credit Score Requirements</li>
      <li>No Loss of Ownership</li>
    </ul>

    <p class="payout">Receive Cash by Lump Sum,<br>Monthly Installments<br>or a Line of Credit!!</p>

    <div class="company">
      <p class="company-name">Bluegate Financial Services, Inc.</p>
      <p class="company-license">NMLS #318760</p>
    </div>

    <div class="contact">
      <p class="contact-cta">Call us today for a Free Consultation!!</p>
      <p class="contact-phone">(800) 471-2965</p>
    </div>

    <svg class="collage" viewBox="0 0 625 625">
      <defs>
        <linearGradient id="tone-couple" x1="0" y1="0" x2="1" y2="1">
          <stop offset="0" stop-color="var(--sky)"/>
          <stop offset="0.45" stop-color="var(--skin-warm)"/>
          <stop offset="1" stop-color="var(--shirt-light)"/>
        </linearGradient>
        <linearGradient id="tone-portrait" x1="0" y1="0" x2="1" y2="1">
          <stop offset="0" stop-color="#cfe3ea"/>
          <stop offset="0.5" stop-color="var(--skin-deep)"/>
          <stop offset="1" stop-color="#8fb6c8"/>
        </linearGradient>
        <linearGradient id="tone-beach" x1="0" y1="0" x2="1" y2="1">
          <stop offset="0" stop-color="#b9d8e8"/>
          <stop offset="0.5" stop-color="var(--skin-warm)"/>
          <stop offset="1" stop-color="#f1efe9"/>
        </linearGradient>
        <linearGradient id="tone-phone" x1="0" y1="0" x2="1" y2="1">
          <stop offset="0" stop-color="#b0352c"/>
          <stop offset="0.5" stop-color="#b98a5e"/>
          <stop offset="1" stop-color="#e9e2d6"/>
        </linearGradient>
        <linearGradient id="tone-outdoor" x1="0" y1="0" x2="1" y2="1">
          <stop offset="0" stop-color="#d8d2c4"/>
          <stop offset="0.5" stop-color="var(--skin-deep)"/>
          <stop offset="1" stop-color="#6f8fb0"/>
        </linearGradient>
      </defs>

      <polygon points="400,290 500,395 400,500 300,395" fill="var(--brand-blue)"/>
      <polygon points="580,392 625,437 625,520 572,468" fill="var(--brand-blue)"/>
      <polygon points="18,530 60,530 38,562" fill="var(--brand-blue)"/>

      <polygon class="photo" role="img" aria-label="Photo: smiling senior couple embracing"
        points="318,288 465,420 330,577 185,440" fill="url(#tone-couple)"/>
      <polygon class="photo" role="img" aria-label="Photo: thoughtful senior man resting chin on hand"
        points="540,266 625,330 625,440 575,462 440,380" fill="url(#tone-portrait)"/>
      <polygon class="photo" role="img" aria-label="Photo: senior couple smiling at the beach"
        points="490,437 585,510 520,577 370,577 360,545" fill="url(#tone-beach)"/>
      <polygon class="photo" role="img" aria-label="Photo: senior couple relaxing outdoors"
        points="0,400 42,370 125,460 42,548 0,510" fill="url(#tone-outdoor)"/>
      <polygon class="photo" role="img" aria-label="Photo: woman checking her phone at home"
        points="158,440 250,530 205,577 110,577 68,532" fill="url(#tone-phone)"/>
    </svg>

    <p class="web-band">www.bluegatehome.com</p>
  </article>
</main>
</body>
</html>
```